New web design for a service provider in the medical field

We are looking for a new design for our website. We are a company that repairs and sells medical endoscopes. Our customers include doctors and hospitals. Our current website can be found at https://lumenfix.example/en/lumenfix-english.
We need a new web design (without programming) for the following 3 pages:
-Startpage https://lumenfix.example/en/lumenfix-english/
-Used endoscopes https://lumenfix.example/en/used-endoscopes/
-Purchase https://lumenfix.example/en/purchase/
The design should be modern and stylish.
The blue color of the logo should be reflected on the page, but not too intrusive.
I have uploaded the images from the header. If more images are needed, let me know and I will upload them.

Target Market(s)
Doctors and hospitals

```html
<!DOCTYPE html>
<html lang="en">
<head>
<meta charset="utf-8">
<title>LumenFix – Endoscope Repair</title>
<link href="https://fonts.googleapis.com/css2?family=Lexend:wght@300;400;500;600;700&family=Roboto:wght@400;500;700&display=swap" rel="stylesheet">
<style>
:root{
  --blue:#2aa6e6;
  --blue-light:#4cb8f0;
  --navy:#173a5a;
  --navy-deep:#13304b;
  --text:#2b3a4a;
  --muted:#5b6775;
  --pale:#e8f1f8;
  --pale-2:#dde9f3;
  --white:#ffffff;
  --line:#b9d6ea;
}
*{box-sizing:border-box;margin:0;padding:0}
html,body{width:1200px;height:4996px;overflow:hidden}
body{font-family:"Roboto",Arial,sans-serif;color:var(--text);background:var(--white);position:relative}
h1,h2,h3,h4,.head{font-family:"Lexend",Arial,sans-serif}
section,header,footer{position:absolute;left:0;width:1200px}
.abs{position:absolute}
.btn{position:absolute;display:flex;align-items:center;justify-content:center;font-family:"Lexend",sans-serif;font-size:13px;font-weight:500;letter-spacing:.3px;white-space:nowrap}
.btn-outline{border:2px solid var(--blue);color:var(--navy);background:var(--white)}
.brand{font-family:"Lexend",sans-serif;font-weight:500;color:var(--navy);font-size:24px;display:flex;align-items:center;gap:10px}
.brand .dot{width:14px;height:14px;border-radius:50%;background:var(--blue)}

/* header */
.site-header{top:0;height:120px;background:var(--white)}
.topbar{position:absolute;right:0;top:0;width:510px;height:46px;background:var(--blue);border-bottom-left-radius:24px;color:#fff;font-size:12px;font-weight:500;display:flex;align-items:center;gap:24px;padding-left:22px;white-space:nowrap}
.topbar span{display:flex;align-items:center;gap:8px}
.topbar i{width:18px;height:18px;border-radius:50%;background:#fff;display:inline-block}
.main-nav{position:absolute;left:300px;top:78px;display:flex;gap:29px;font-family:"Lexend",sans-serif;font-size:12px;font-weight:600;color:var(--navy);white-space:nowrap}
.main-nav a{text-decoration:none;color:inherit;padding-bottom:8px}
.main-nav a.active{border-bottom:2px solid var(--blue)}

/* hero */
.hero{top:120px;height:575px;background:linear-gradient(100deg,#e9eff5 0%,#d8e3ee 55%,#c9d6e2 100%)}
.hero-photo{position:absolute;right:0;top:0;width:560px;height:575px;background:linear-gradient(160deg,#dfe6ee,#b5c2cf 70%,#7d8894)}
.hero .eyebrow{position:absolute;left:102px;top:178px;font-family:"Lexend";font-size:17px;letter-spacing:3px;color:var(--blue)}
.hero h1{position:absolute;left:102px;top:208px;font-size:38px;line-height:48px;font-weight:700;color:var(--navy)}

/* service band */
.service-band{top:695px;height:490px;background:linear-gradient(100deg,#1f8fd2,#2aa6e6 60%,#3aa9e5)}
.service-band h2{position:absolute;left:115px;top:98px;color:#fff;font-size:38px;font-weight:300;line-height:46px}
.service-band h2 b{font-weight:600}
.service-band .rule{position:absolute;left:122px;top:196px;width:80px;height:3px;background:#fff}
.service-band p{position:absolute;left:456px;top:88px;width:610px;color:#fff;font-size:16px;line-height:27px}
.intro{top:1000px;height:470px}
.intro-photo{position:absolute;left:101px;top:0;width:548px;height:470px;background:linear-gradient(135deg,#eef0f2,#9ca3aa 60%,#5d6369)}
.intro-card{position:absolute;left:560px;top:44px;width:545px;height:398px;background:#fff;box-shadow:0 6px 30px rgba(20,50,80,.12);padding:44px 50px}
.intro-card h3{font-size:22px;line-height:29px;font-weight:400;color:var(--navy)}
.intro-card .rule{width:66px;height:2px;background:var(--blue);margin:14px 0 22px}
.intro-card p{font-size:13.5px;line-height:21px;color:var(--text);margin-bottom:12px}
.intro-accent{position:absolute;left:887px;top:426px;width:230px;height:6px;background:var(--blue)}
.intro-accent-v{position:absolute;left:1108px;top:280px;width:4px;height:150px;background:var(--blue)}

/* services diagram */
.services{top:1490px;height:490px}
.svc{position:absolute;width:260px;text-align:center}
.svc h4{font-size:18px;font-weight:600;color:var(--navy);margin-top:14px}
.svc .sub{font-size:14px;color:var(--muted);margin-top:4px}
.svc p{font-size:11px;line-height:19px;color:var(--muted);margin-top:16px;padding:0 20px}
.svc .btn{position:relative;margin:16px auto 0;width:204px;height:44px}

/* faulty */
.faulty{top:2080px;height:570px}
.faulty h2{position:absolute;left:108px;top:136px;color:#fff;font-size:32px;font-weight:300}
.faulty h2 b{font-weight:600}
.faulty .lead{position:absolute;left:108px;top:200px;color:#fff;font-family:"Lexend";font-size:22px}
.faulty p{position:absolute;left:108px;top:242px;width:420px;color:#fff;font-size:15px;line-height:25px}
.faulty .btn{left:114px;top:373px;width:178px;height:52px;background:var(--blue);color:#fff}

/* benefits grid */
.benefits{top:2700px;height:680px}
.benefits h2{position:absolute;left:0;width:1200px;top:30px;text-align:center;font-size:32px;font-weight:600;color:var(--navy);letter-spacing:.5px}
.benefits h2 span{color:var(--blue)}
.benefits .rule{position:absolute;left:553px;top:84px;width:80px;height:3px;background:var(--blue)}
.cell{position:absolute;width:310px;height:245px;padding:34px 40px}
.cell h4{font-size:18px;font-weight:600;color:var(--navy);line-height:22px;margin-top:14px}
.cell p{font-size:14px;line-height:20px;color:var(--muted);margin-top:10px}
.cell.hl{background:linear-gradient(135deg,#1c7fc4,#2aa6e6);color:#fff}
.cell.hl h4,.cell.hl p{color:#fff}

/* decision */
.decision{top:3400px;height:640px;background:var(--pale)}
.decision h2{position:absolute;left:0;width:1200px;top:76px;text-align:center;font-size:26px;line-height:32px;font-weight:600;color:var(--navy)}
.decision .rule{position:absolute;left:563px;top:146px;width:74px;height:3px;background:var(--blue)}
.feat{position:absolute;width:300px}
.feat h5{font-family:"Lexend";font-size:14px;font-weight:600;color:var(--navy)}
.feat p{font-size:10.5px;line-height:16px;color:var(--muted);margin-top:5px}
.feat.l{text-align:right}
.decision .btn{left:486px;top:510px;width:276px;height:46px;background:var(--blue);color:#fff;border-radius:0 0 0 22px;border-top-right-radius:22px}

/* contact */
.contact{top:4040px;height:580px;background:linear-gradient(90deg,#dbe4ec 0%,#f5f8fa 55%,#fff 100%)}
.contact-photo{position:absolute;left:0;top:0;width:560px;height:580px;background:linear-gradient(120deg,#cfd9e2,#e9eef2 50%,#b8c6d2)}
.contact h2{position:absolute;left:625px;top:108px;font-size:30px;font-weight:600;color:var(--navy)}
.contact h2 span{color:var(--blue)}
.field{position:absolute;left:630px;width:422px;height:46px;border:1.5px solid #b9c7d3;background:#fff;display:flex;align-items:center;padding-left:20px;gap:12px;font-size:12px;font-weight:500;color:var(--navy)}
.field i{width:10px;height:10px;border-radius:50%;border:1.5px solid #8fa1b0}
.field.area{height:80px;align-items:flex-start;padding-top:16px}
.contact .btn{left:634px;top:490px;width:160px;height:42px;background:var(--navy);color:#fff;font-size:12px}

/* footer */
.site-footer{top:4620px;height:376px;background:var(--blue);color:#fff}
.site-footer .brand{color:#fff;position:absolute;left:110px;top:90px}
.site-footer .brand .dot{background:#fff}
.site-footer .about{position:absolute;left:110px;top:160px;width:270px;font-size:12px;line-height:16px;color:#d6eefb}
.fcol{position:absolute;top:56px;border-left:2px solid #fff;padding-left:18px;height:24px}
.fcol h6{font-family:"Lexend";font-size:14px;font-weight:600;letter-spacing:.5px}
.fcol ul{list-style:none;margin-top:22px;margin-left:-20px;padding-left:0;white-space:nowrap}
.fcol li{font-size:13px;line-height:29px}
.signup{position:absolute;left:886px;top:56px}
.signup h6{font-family:"Lexend";font-size:14px;font-weight:600}
.signup .input{width:214px;height:36px;background:#fff;margin-top:18px;color:var(--muted);font-size:11px;padding:12px 16px}
.signup .sub{width:214px;height:36px;background:var(--navy);margin-top:10px;display:flex;align-items:center;justify-content:center;font-family:"Lexend";font-size:12px;font-weight:600}
.social{display:flex;gap:8px;margin-top:16px}
.social i{width:28px;height:28px;border-radius:50%;background:#fff;display:block}
.copy{position:absolute;left:0;width:1200px;top:336px;text-align:center;font-size:12px;color:#e3f3fc}
</style>
</head>
<body>

<header class="site-header">
  <div class="brand" style="position:absolute;left:96px;top:32px"><span class="dot"></span>LumenFix</div>
  <div class="topbar">
    <span><i></i>info@lumenfix.example</span>
    <span><i></i>+49 000 555 0140</span>
    <span>ENG</span>
  </div>
  <nav class="main-nav">
    <a class="active" href="https://lumenfix.example/en/lumenfix-english/">ENDOSCOPE REPAIR</a>
    <a href="https://lumenfix.example/en/used-endoscopes/">ENDOSCOPY SYSTEMS</a>
    <a href="#">ENDOSCOPY ACCESSORIES</a>
    <a href="#" style="margin-left:14px">ACCESSORIES CATALOG</a>
    <a href="https://lumenfix.example/en/purchase/" style="margin-left:14px">PURCHASE</a>
  </nav>
</header>

<section class="hero">
  <div class="hero-photo" role="img" aria-label="Photo of two white flexible endoscope control handles with black cables"></div>
  <div class="eyebrow">WELCOME TO LUMENFIX</div>
  <h1>PUT YOUR ENDOSCOPE<br>IN RELIABLE HANDS!</h1>
  <div class="btn btn-outline" style="left:106px;top:324px;width:180px;height:52px;background:transparent;color:var(--blue);font-size:15px;font-weight:400">LEARN MORE</div>
</section>

<section class="service-band">
  <h2>YOUR FUTURE<br><b>OUR SERVICE</b></h2>
  <div class="rule"></div>
  <p>LumenFix GmbH is specialised in the repair and sale of Orvane, Pextra and Fujara flexible medical endoscopes. As a service-oriented company, we are certified according to DIN ISO 9001:2015 and we are at your side with our knowledge and skills!</p>
</section>

<section class="intro">
  <div class="intro-photo" role="img" aria-label="Close-up photo of an endoscope control body with angulation knobs"></div>
  <div class="intro-accent-v"></div>
  <div class="intro-card">
    <h3>Endoscope repairs and second hand endoscopes from LumenFix&nbsp; cause the outcome matters!</h3>
    <div class="rule"></div>
    <p>LumenFix is a privileged partner for the start-up facility or optimisation of existing healthcare facilities, doctor's offices and hospitals. The quality and reliability of our products and our offered service are our best advertisement!</p>
    <p>As a result of optimised processes and highly qualified specialists in our company, we can work very quickly and with high quality for your benefit of least possible restrictions in your doctor's office or in your hospital.</p>
  </div>
  <div class="intro-accent"></div>
  <svg class="abs" style="left:945px;top:452px" width="190" height="30">
    <g fill="#9cc9e6">
      <circle cx="5" cy="5" r="2"/><circle cx="25" cy="5" r="2"/><circle cx="45" cy="5" r="2"/><circle cx="65" cy="5" r="2"/><circle cx="85" cy="5" r="2"/><circle cx="105" cy="5" r="2"/><circle cx="125" cy="5" r="2"/><circle cx="145" cy="5" r="2"/><circle cx="165" cy="5" r="2"/>
      <circle cx="5" cy="25" r="2"/><circle cx="25" cy="25" r="2"/><circle cx="45" cy="25" r="2"/><circle cx="65" cy="25" r="2"/><circle cx="85" cy="25" r="2"/><circle cx="105" cy="25" r="2"/><circle cx="125" cy="25" r="2"/><circle cx="145" cy="25" r="2"/><circle cx="165" cy="25" r="2"/>
    </g>
  </svg>
</section>

<section class="services">
  <svg class="abs" style="left:0;top:0" width="1200" height="240">
    <g fill="none" stroke="#2aa6e6" stroke-width="2">
      <path d="M600 22 V68 M272 68 H925 M272 68 V104 M925 68 V104 M600 68 V104"/>
    </g>
    <g>
      <rect x="227" y="120" width="90" height="90" transform="rotate(45 272 165)" fill="#2aa6e6"/>
      <rect x="233" y="126" width="78" height="78" transform="rotate(45 272 165)" fill="none" stroke="#fff" stroke-width="2"/>
      <rect x="555" y="120" width="90" height="90" transform="rotate(45 600 165)" fill="#173a5a"/>
      <rect x="561" y="126" width="78" height="78" transform="rotate(45 600 165)" fill="none" stroke="#fff" stroke-width="2"/>
      <rect x="880" y="120" width="90" height="90" transform="rotate(45 925 165)" fill="#2aa6e6"/>
      <rect x="886" y="126" width="78" height="78" transform="rotate(45 925 165)" fill="none" stroke="#fff" stroke-width="2"/>
    </g>
    <g fill="none" stroke="#fff" stroke-width="2.5">
      <circle cx="266" cy="165" r="16"/><circle cx="266" cy="165" r="9"/><path d="M282 165 H298"/>
      <circle cx="604" cy="159" r="12"/><path d="M596 169 L588 183"/>
      <rect x="916" y="147" width="18" height="24" rx="3"/><path d="M925 171 V185"/>
    </g>
  </svg>
  <div class="svc" style="left:143px;top:248px">
    <h4>REPAIR</h4><div class="sub">Endoscope repair service</div>
    <p>Manufacturer-independent we repair and maintain endoscopes, individual components (e.g. processors or light sources), accessories and peripherals of the manufacturers Orvane, Pextra and Fujara.</p>
    <div class="btn btn-outline">REPAIR REQUEST</div>
  </div>
  <div class="svc" style="left:470px;top:248px">
    <h4>SALE</h4><div class="sub">Used endoscopes</div>
    <p>Our regular stock includes refurbished gastroscopes, colonoscopes, bronchoscopes, cystoscopes and duodenoscopes from the well-known manufacturers Orvane, Pextra and Fujara.</p>
    <div class="btn btn-outline" style="margin-top:35px">PURCHASE REQUEST</div>
  </div>
  <div class="svc" style="left:795px;top:248px">
    <h4>PURCHASE</h4><div class="sub">Used endoscopes</div>
    <p>We are very interested in buying your old endoscopes – even defective and dismantled! We offer fair conditions! Please contact us for a purchase offer!</p>
    <div class="btn btn-outline" style="margin-top:35px">SELL DEVICE</div>
  </div>
</section>

<section class="faulty">
  <svg class="abs" style="left:0;top:0" width="1200" height="570">
    <defs><linearGradient id="fg" x1="0" y1="0" x2="1" y2="1"><stop offset="0" stop-color="#1f8fd2"/><stop offset="1" stop-color="#3cb2ef"/></linearGradient></defs>
    <rect width="1200" height="570" fill="#173a5a"/>
    <polygon points="925,0 1200,0 1200,570 610,570" fill="url(#fg)"/>
    <circle cx="830" cy="270" r="196" fill="none" stroke="#9cc9e6" stroke-width="1.5"/>
    <circle cx="830" cy="270" r="176" fill="none" stroke="#ffffff" stroke-opacity=".5" stroke-width="1.5"/>
  </svg>
  <div class="abs" role="img" aria-label="Photo of a dark endoscope handpiece close-up" style="left:664px;top:104px;width:332px;height:332px;border-radius:50%;background:radial-gradient(circle at 40% 40%,#f4f6f8,#c8d0d8 70%,#8d98a3)"></div>
  <h2>FAULTY <b>ENDOSCOPE?</b></h2>
  <div class="lead">We ensure quick and smooth repairs!</div>
  <p>Lorem ipsum dolor sit amet, consectetur adipiscing elit, sed do eiusmod tempor incididunt ut labore et dolore magna aliqua. Ut enim ad minim veniam, quis nostrud exercitation ullamco laboris n</p>
  <div class="btn">PLACE ORDER&nbsp;›</div>
</section>

<section class="benefits">
  <h2>CAUSE THE <span>OUTCOME MATTERS</span></h2>
  <div class="rule"></div>
  <svg class="abs" style="left:0;top:0" width="1200" height="680">
    <g stroke="#b9d6ea" stroke-width="1.5">
      <path d="M124 388 H1072"/><path d="M430 140 V640"/><path d="M762 140 V640"/>
    </g>
  </svg>
  <div class="cell hl" style="left:124px;top:140px;height:245px">
    <svg width="44" height="44" viewBox="0 0 44 44" fill="none" stroke="#fff" stroke-width="2"><circle cx="22" cy="22" r="14"/><circle cx="22" cy="18" r="4"/><path d="M14 30 q8-8 16 0"/></svg>
    <h4 style="margin-top:30px">One company for everyone</h4>
    <p>We are a service provider for doctors and hospitals!</p>
  </div>
  <div class="cell" style="left:450px;top:148px">
    <svg width="56" height="56" viewBox="0 0 56 56" fill="none" stroke="#173a5a" stroke-width="2"><circle cx="28" cy="14" r="7"/><circle cx="16" cy="36" r="6"/><circle cx="40" cy="36" r="6"/><path d="M6 54 q10-14 20 0 M30 54 q10-14 20 0"/></svg>
    <h4>Experience characteristics us</h4>
    <p>Our team has many years of experience in the business field!</p>
  </div>
  <div class="cell" style="left:780px;top:148px">
    <svg width="56" height="56" viewBox="0 0 56 56" fill="none" stroke="#173a5a" stroke-width="2"><rect x="18" y="4" width="14" height="22" rx="3"/><path d="M25 26 V46 q0 8 10 8"/><circle cx="25" cy="14" r="3" stroke="#2aa6e6"/></svg>
    <h4>The product is close to our hearts</h4>
    <p>We repair and sell second hand, flexible endoscopes!</p>
  </div>
  <div class="cell" style="left:130px;top:410px">
    <svg width="44" height="50" viewBox="0 0 44 50" fill="none" stroke="#2aa6e6" stroke-width="2"><path d="M22 2 L40 9 V24 q0 16-18 24 q-18-8-18-24 V9z"/><circle cx="22" cy="24" r="8"/><path d="M18 24 l3 3 l5-6"/></svg>
    <h4>Guaranteed service</h4>
    <p>You receive a six-month warranty on all repairs!</p>
  </div>
  <div class="cell" style="left:455px;top:420px">
    <svg width="60" height="50" viewBox="0 0 60 50" fill="none" stroke="#2aa6e6" stroke-width="2"><path d="M30 2 l4 8 9 1 -7 6 2 9 -8-5 -8 5 2-9 -7-6 9-1z"/><path d="M4 34 h14 q6 0 10 4 h14 l14-8 v6 l-14 10 h-38z"/></svg>
    <h4>Quality not quantity</h4>
    <p>Reliability and durability instead of inferior replacements!</p>
  </div>
  <div class="cell" style="left:785px;top:418px">
    <svg width="52" height="56" viewBox="0 0 52 56" fill="none" stroke="#2aa6e6" stroke-width="2"><path d="M22 2 L40 9 V24 q0 16-18 24 q-18-8-18-24 V9z"/><circle cx="36" cy="40" r="9" stroke="#173a5a"/><path d="M15 22 l5 5 9-10"/></svg>
    <h4>Services for everyone</h4>
    <p>Our service includes the manufacturers Orvane, Pextra and Fujara!</p>
  </div>
</section>

<section class="decision">
  <h2>LUMENFIX GMBH, YOUR DECISION<br>FOR YOUR FUTURE</h2>
  <div class="rule"></div>
  <svg class="abs" style="left:0;top:0" width="1200" height="640">
    <defs><linearGradient id="cg" x1="0" y1="0" x2="1" y2="1"><stop offset="0" stop-color="#1f8fd2"/><stop offset="1" stop-color="#3cb2ef"/></linearGradient></defs>
    <circle cx="608" cy="325" r="138" fill="none" stroke="#2aa6e6" stroke-width="2"/>
    <circle cx="608" cy="325" r="118" fill="url(#cg)"/>
    <g stroke="#2aa6e6" stroke-width="2">
      <path d="M432 205 L516 224 M432 325 L470 325 M432 440 L516 420 M784 205 L700 224 M784 325 L746 325 M784 440 L700 420"/>
    </g>
    <g fill="#2aa6e6"><circle cx="516" cy="224" r="5"/><circle cx="470" cy="325" r="5"/><circle cx="516" cy="420" r="5"/><circle cx="700" cy="224" r="5"/><circle cx="746" cy="325" r="5"/><circle cx="700" cy="420" r="5"/></g>
    <g>
      <circle cx="412" cy="205" r="30" fill="#2aa6e6"/><circle cx="405" cy="325" r="30" fill="#173a5a"/><circle cx="412" cy="440" r="30" fill="#2aa6e6"/>
      <circle cx="804" cy="205" r="30" fill="#173a5a"/><circle cx="808" cy="325" r="30" fill="#2aa6e6"/><circle cx="810" cy="440" r="30" fill="#173a5a"/>
    </g>
    <g fill="none" stroke="#fff" stroke-width="2">
      <path d="M400 193 l24 24 M424 193 l-24 24"/>
      <circle cx="405" cy="325" r="10"/><circle cx="405" cy="325" r="4"/>
      <rect x="400" y="428" width="24" height="24" rx="2"/>
      <circle cx="804" cy="202" r="9"/><path d="M792 218 h24"/>
      <path d="M798 332 l10-16 10 16z"/>
      <path d="M810 432 l3 6 6 1 -5 4 2 6 -6-3 -6 3 2-6 -5-4 6-1z"/>
    </g>
  </svg>
  <div class="abs" style="left:490px;top:310px;width:236px;text-align:center;font-family:'Lexend';font-size:24px;font-weight:500;color:#fff">LumenFix</div>
  <div class="abs" style="left:490px;top:344px;width:236px;text-align:center;font-size:10px;color:#d6eefb">Repair you can rely on</div>
  <div class="feat l" style="left:60px;top:182px"><h5>Fast Repairs</h5><p>Keep potential disruptions in your doctor's office or in your hospital at minimum</p></div>
  <div class="feat l" style="left:60px;top:296px"><h5>On-site service</h5><p>We will gladly pay you a visit to carry out analysis and repairs on site. Due to our many years of experience</p></div>
  <div class="feat l" style="left:60px;top:422px"><h5>Without a maintenance contract</h5><p>No subscription or other maintenance contract, but one-time and sustainable repair work</p></div>
  <div class="feat" style="left:850px;top:182px"><h5>Highly cost efficient</h5><p>Benefit from our first class recommendations and implementation by our experienced staff.</p></div>
  <div class="feat" style="left:850px;top:292px"><h5>Loan equipment service</h5><p>We will gladly pay you a visit to carry out analysis and repairs on site. Due to our many years of experience</p></div>
  <div class="feat" style="left:850px;top:428px"><h5>First class service</h5><p>Our clients always come first!</p></div>
  <div class="btn">Learn more about LumenFix</div>
</section>

<section class="contact">
  <div class="contact-photo" role="img" aria-label="Photo of a doctor in a white coat working at a laptop"></div>
  <h2>HOW CAN WE <span>HELP YOU?</span></h2>
  <div class="field" style="top:178px"><i></i>First name</div>
  <div class="field" style="top:232px"><i></i>Phone number</div>
  <div class="field" style="top:286px"><i></i>Email address</div>
  <div class="field area" style="top:342px">Comments</div>
  <div class="btn">SUBMIT NOW</div>
</section>

<footer class="site-footer">
  <div class="brand"><span class="dot"></span>LumenFix</div>
  <div class="about">Lorem ipsum dolor sit amet, consectetur adipiscing elit, sed do eiusmod</div>
  <div class="fcol" style="left:416px"><h6>NAVIGATION</h6>
    <ul><li>Home</li><li>Endoscope Repair</li><li>Used Endoscope</li><li>Endoscopy Systems</li></ul></div>
  <div class="fcol" style="left:652px"><h6>RESOURCES</h6>
    <ul><li>Endoscopy Accesories</li><li>Purchase</li><li>Contact Us</li></ul></div>
  <div class="fcol" style="left:862px;height:24px"></div>
  <div class="signup"><h6>SIGN UP EMAIL</h6>
    <div class="input">Email address</div>
    <div class="sub">SUBSCRIBE</div>
    <div class="social"><i></i><i></i><i></i><i></i></div>
  </div>
  <div class="copy">© 2022 LumenFix GmbH</div>
</footer>

</body>
</html>
```